Box Design of "pet rapid test for dogs & cats" with professional use

"The market is in Southeast Asia, South America, Europe, and the U.S."
Clients: Veterinary clinics, pet hospitals,(a small number of home use)

Primary colors:
Orange, Green,or Blue, (select 1,or 2 color)
Neutrals: Black, Gray, or White (optional)
Dimensions:135mm(L)*90mm(W)*105mm(W)

Kindly review the attached file for additional content
Updates

I have increased my budget, please provide a satisfactory design solution, thank you very much for your work.

Target Market(s)

Southeast Asia, South America, Europe, and the U.S.

Industry/Entity Type

Veterinary test kit for dogs & cats

Colors
0054AA
0677BA
7BADD7
CADEEF
E8F1F8
0094D4
00A9DD
6FCCEA
C7EBF8
E9F6FB
00AB8E
00BBA5
67D7C9
C6EFE9
E9F9F6
59FF00
82FF00
B8FF75
E3FFCB
F4FFEA
F0912C
F2A743
F7CA91
FBE8D2
FDF5EE
EE7325
F08F49
F5BC92
FAE3D3
FDF4ED

Requirements
Nice to have
• Appealing Box Appearance with professional

```html
<!DOCTYPE html>
<html lang="en">
<head>
<meta charset="UTF-8">
<title>Tailsure Rapid Test Kit – Box Front</title>
<link href="https://fonts.googleapis.com/css2?family=Poppins:wght@300;400;500;600;700&display=swap" rel="stylesheet">
<style>
  :root {
    --stage: #97bbbe;
    --teal: #287c7b;
    --mint: #dcedea;
    --orange: #ec963c;
    --ink: #161616;
    --white: #ffffff;
  }
  * { margin: 0; padding: 0; box-sizing: border-box; }
  html, body { width: 1200px; height: 1200px; overflow: hidden; }
  body {
    background: var(--stage);
    font-family: "Poppins", sans-serif;
    position: relative;
  }
  .brand-column {
    position: absolute; left: 40px; top: 40px;
    width: 400px; height: 1120px;
    display: flex; flex-direction: column;
  }
  .brand-tile {
    flex: 1;
    display: flex; flex-direction: column; align-items: center; justify-content: center;
    gap: 22px;
  }
  .brand-tile--light { background: var(--mint); color: var(--teal); }
  .brand-tile--dark { background: var(--teal); color: var(--white); }
  .brand-mark {
    width: 84px; height: 84px; border-radius: 50%;
    border: 6px solid currentColor;
  }
  .brand-name { font-size: 58px; font-weight: 600; letter-spacing: 1px; line-height: 1; }

  .front-panel {
    position: absolute; left: 470px; top: 40px;
    width: 690px; height: 1120px;
    background: var(--mint);
    overflow: hidden;
  }
  .front-header {
    background: var(--teal);
    height: 420px;
    display: flex; flex-direction: column; align-items: center; justify-content: center;
    color: var(--white); text-align: center;
  }
  .product-title { font-size: 62px; font-weight: 600; line-height: 1.1; letter-spacing: 1px; }
  .product-subtitle { font-size: 46px; font-weight: 400; line-height: 1.3; letter-spacing: 2px; margin-top: 8px; }
  .tagline-pill {
    margin-top: 34px;
    background: var(--orange); border-radius: 12px;
    padding: 6px 44px;
    font-size: 30px; font-weight: 300; letter-spacing: 1px;
  }

  .pet-silhouette {
    position: absolute; right: -80px; top: 470px;
    width: 360px; height: 560px;
    border-radius: 48% 52% 30% 40% / 40% 40% 30% 30%;
    background: radial-gradient(circle at 50% 45%, rgba(169,200,202,0.55), rgba(169,200,202,0.15) 70%);
  }

  .contents {
    position: absolute; left: 40px; top: 500px; width: 620px;
    color: var(--ink);
  }
  .contents-heading { font-size: 30px; font-weight: 500; margin-bottom: 16px; }
  .contents-list { list-style: none; font-size: 23px; font-weight: 300; line-height: 1.65; }
  .contents-list li { display: flex; gap: 22px; white-space: nowrap; }
  .contents-list .num { width: 16px; }
  .storage-note { font-size: 23px; font-weight: 300; margin: 12px 0 0 38px; }

  .symbol-row {
    position: absolute; left: 40px; top: 960px;
    display: flex; align-items: center; gap: 22px;
  }
  .ivd-box {
    border: 4px solid var(--ink); padding: 4px 10px;
    font-size: 32px; font-weight: 700; line-height: 1; color: var(--ink);
  }
  .symbol-row svg { display: block; }

  .count-badge {
    position: absolute; right: 0; bottom: 70px;
    width: 150px; height: 150px;
    background: var(--orange); border-radius: 22px 0 0 22px;
    color: var(--white); text-align: center;
    display: flex; flex-direction: column; justify-content: center;
  }
  .count-badge .count { font-size: 66px; font-weight: 600; line-height: 1; }
  .count-badge .unit { font-size: 22px; font-weight: 600; }
</style>
</head>
<body>
  <section class="brand-column">
    <div class="brand-tile brand-tile--light">
      <span class="brand-mark"></span>
      <span class="brand-name">TAILSURE</span>
    </div>
    <div class="brand-tile brand-tile--dark">
      <span class="brand-mark"></span>
      <span class="brand-name">TAILSURE</span>
    </div>
  </section>

  <section class="front-panel">
    <header class="front-header">
      <h1 class="product-title">PET RAPID TEST KIT</h1>
      <p class="product-subtitle">For Dogs &amp; Cats</p>
      <p class="tagline-pill">Loved by Pets, Trusted by Vets</p>
    </header>

    <div class="pet-silhouette" role="img" aria-label="Faint outline illustration of a dog and cat"></div>

    <div class="contents">
      <h2 class="contents-heading">Contents</h2>
      <ol class="contents-list">
        <li><span class="num">1</span>Test Kits (cassette, disposable dropper, desiccant).</li>
        <li><span class="num">2</span>Assay buffer.</li>
        <li><span class="num">3</span>Sterile swabs.</li>
        <li><span class="num">4</span>Instruction manual.</li>
      </ol>
      <p class="storage-note">Store at 2–30°C.</p>
    </div>

    <div class="symbol-row">
      <span class="ivd-box">IVD</span>
      <svg width="108" height="80" viewBox="0 0 108 80" aria-label="Temperature limit 2 to 30 degrees C">
        <text x="0" y="77" font-family="Poppins, sans-serif" font-size="15" fill="#161616">2°C</text>
        <text x="66" y="17" font-family="Poppins, sans-serif" font-size="15" fill="#161616">30°C</text>
        <line x1="28" y1="72" x2="40" y2="72" stroke="#161616" stroke-width="2"/>
        <line x1="54" y1="12" x2="64" y2="12" stroke="#161616" stroke-width="2"/>
        <line x1="40" y1="72" x2="54" y2="12" stroke="#161616" stroke-width="4"/>
        <circle cx="40" cy="72" r="6" fill="#161616"/>
      </svg>
      <svg width="70" height="70" viewBox="0 0 70 70" aria-label="Keep away from sunlight">
        <circle cx="35" cy="22" r="6" fill="#161616"/>
        <g stroke="#161616" stroke-width="2">
          <line x1="35" y1="4" x2="35" y2="12"/><line x1="17" y1="22" x2="25" y2="22"/>
          <line x1="45" y1="22" x2="53" y2="22"/><line x1="22" y1="9" x2="28" y2="15"/>
          <line x1="48" y1="9" x2="42" y2="15"/><line x1="10" y1="50" x2="60" y2="8"/>
        </g>
        <polyline points="20,52 35,40 50,52" fill="none" stroke="#161616" stroke-width="3"/>
        <rect x="30" y="52" width="10" height="12" fill="#161616"/>
      </svg>
      <svg width="60" height="50" viewBox="0 0 60 50" aria-label="Consult instructions for use">
        <path d="M4 8 L28 4 L28 44 L4 48 Z M56 8 L32 4 L32 44 L56 48 Z" fill="none" stroke="#161616" stroke-width="3"/>
        <rect x="40" y="12" width="6" height="6" fill="#161616"/>
        <rect x="40" y="22" width="6" height="16" fill="#161616"/>
      </svg>
      <svg width="64" height="64" viewBox="0 0 64 64" aria-label="Do not reuse">
        <circle cx="32" cy="32" r="28" fill="none" stroke="#161616" stroke-width="3"/>
        <line x1="12" y1="52" x2="52" y2="12" stroke="#161616" stroke-width="3"/>
        <path d="M22 24 Q32 12 40 22 Q44 30 22 46 L44 46" fill="none" stroke="#161616" stroke-width="3"/>
      </svg>
    </div>

    <div class="count-badge">
      <span class="count">10</span>
      <span class="unit">Tests/box</span>
    </div>
  </section>
</body>
</html>
```